Business Card design for amazing new Dental Office

Please read this brief closely!

Our client is a modern new dental office/
They love their new logo.
Now it's time to create a business card for them.

It should be a two sided card:
Side one should have the logo and name and maybe a color background or design.
Side two should have all the contact information which is here:

Marcus Holloway, D.D.S
General and Cosmetic Dentistry
4187 W. Pinecrest Avenue
Ventura, CA 93011
(805) 912-4386
drmarcus@bluefernsmiles-example.com
www.bluefernsmiles-example.com

Feel free to arrange that info as you like and to style both sides of the card according to your creativity. This is a chance for you to show your design skills!

Client is open to font choices and is looking for a style that is amazing and premium. Colors can be selected from the logo, or any variation of those.

You will not win this contest with a less than beautiful card design so please feel free to make multiple submissions.

Logo files attached and please message me with any questions.
Thanks!

Target Market(s)

Families and Professionals seeking dental services

Industry/Entity Type

Dental

Contact Information for Business Card

Logo, style, contact info as per the brief

Font styles to use
Sans Serif

Requirements
Must have
• Client's logo and contact details as per brief
Nice to have
• Unique style reflecting high end dental clinic near the beach
Should not have
• Must not look like a template

```html
<!DOCTYPE html>
<html lang="en">
<head>
<meta charset="utf-8">
<title>Blue Fern Smiles – Business Card</title>
<link href="https://fonts.googleapis.com/css2?family=Montserrat:wght@300;400;500;700&display=swap" rel="stylesheet">
<style>
  :root{
    --canvas:#ecebe8;
    --card:#ffffff;
    --ink:#3a3a3a;
    --ink-soft:#8a8a8a;
    --rule:#9c9c9c;
    --gold:#d2c24a;
    --sand:#e0a864;
    --teal:#6cc1c4;
    --sea:#3e9fe0;
    --shadow:rgba(0,0,0,.12);
  }
  *{box-sizing:border-box;margin:0;padding:0}
  html,body{width:1200px;height:913px;overflow:hidden;background:var(--canvas)}
  body{position:relative;font-family:"Montserrat",sans-serif;color:var(--ink)}
  .card{
    position:absolute;left:280px;width:640px;height:366px;overflow:hidden;
    background:var(--card);box-shadow:0 6px 22px var(--shadow);
  }
  .card--front{top:64px}
  .card--back{top:483px}

  .wordmark{
    display:flex;align-items:center;gap:12px;
    font-family:"Montserrat",sans-serif;font-weight:400;
    text-transform:uppercase;letter-spacing:.22em;color:var(--ink);
    white-space:nowrap;
  }
  .wordmark__dot{width:16px;height:16px;border-radius:50%;background:var(--teal);flex:none}

  .front-artwork{
    position:absolute;left:0;top:170px;width:430px;height:196px;
    background:
      linear-gradient(to top, rgba(255,255,255,0) 55%, var(--card) 100%),
      linear-gradient(100deg, var(--gold) 0%, var(--sand) 22%, var(--teal) 55%, var(--sea) 100%);
    opacity:.85;
  }
  .card--front .wordmark{position:absolute;right:36px;top:128px;font-size:20px}

  .card--back .wordmark{position:absolute;left:44px;top:172px;font-size:17px}
  .divider{position:absolute;left:318px;top:66px;width:1px;height:234px;background:var(--rule)}
  .details{position:absolute;left:346px;top:70px;width:270px}
  .details__name{font-weight:700;font-size:16px;color:var(--ink-soft);letter-spacing:.01em}
  .details__title{font-weight:300;font-size:12.5px;color:var(--ink-soft);margin-top:3px}
  .details__address{font-weight:500;font-size:11.5px;line-height:1.45;color:var(--ink);margin-top:22px}
  .contact{list-style:none;margin-top:22px}
  .contact li{display:flex;align-items:center;gap:9px;font-size:11px;font-weight:500;color:var(--ink);margin-bottom:7px;white-space:nowrap}
  .contact svg{width:13px;height:13px;flex:none;fill:none;stroke:var(--ink);stroke-width:1.6}
</style>
</head>
<body>

<section class="card card--front" aria-label="Card front">
  <div class="front-artwork" role="img" aria-label="Large sweeping brand artwork in gold, sand, teal and sea blue"></div>
  <div class="wordmark"><span class="wordmark__dot"></span>Blue Fern Smiles</div>
</section>

<section class="card card--back" aria-label="Card back">
  <div class="wordmark"><span class="wordmark__dot"></span>Blue Fern Smiles</div>
  <div class="divider"></div>
  <div class="details">
    <p class="details__name">Marcus Holloway, D.D.S</p>
    <p class="details__title">General and Cosmetic Dentistry</p>
    <p class="details__address">4187 W. Pinecrest Avenue<br>Ventura, CA 93011</p>
    <ul class="contact">
      <li>
        <svg viewBox="0 0 16 16"><path d="M3 1.5h3l1.2 3.3-1.8 1.2a8 8 0 0 0 4.6 4.6l1.2-1.8 3.3 1.2v3a1.5 1.5 0 0 1-1.6 1.5A12.5 12.5 0 0 1 1.5 3.1 1.5 1.5 0 0 1 3 1.5z" fill="var(--ink)" stroke="none"/></svg>
        (805) 912-4386
      </li>
      <li>
        <svg viewBox="0 0 16 16"><rect x="1" y="3" width="14" height="10"/><path d="M1 3l7 6 7-6"/></svg>
        drmarcus@bluefernsmiles-example.com
      </li>
      <li>
        <svg viewBox="0 0 16 16"><circle cx="8" cy="8" r="6.5"/><ellipse cx="8" cy="8" rx="3" ry="6.5"/><path d="M1.5 8h13"/></svg>
        www.bluefernsmiles-example.com
      </li>
    </ul>
  </div>
</section>

</body>
</html>
```